Business Card Design

We are a commercial real estate brokerage in San Francisco, leasing office buildings downtown.
I would like a clean, elegant look. Simple but powerful .

Industry/Entity Type

Business

Contact Information for Business Card

Colin Farrow
lic# 07281549
415.555.0172
colin@tarvo-commercial.example
tarvo-commercial.example

```html
<!DOCTYPE html>
<html lang="en">
<head>
<meta charset="utf-8">
<title>Tarvo Commercial – Business Card</title>
<link rel="stylesheet" href="https://fonts.googleapis.com/css2?family=Arimo:wght@400;700&display=swap">
<style>
  :root {
    --page-bg: #ffffff;
    --card-bg: #ffffff;
    --card-border: #a9a9a9;
    --brand-slate: #74869f;
    --band-top: #54719a;
    --band-bottom: #809ec9;
    --footer-top: #272727;
    --footer-bottom: #000000;
    --text-light: #ffffff;
  }
  * { box-sizing: border-box; margin: 0; padding: 0; }
  html, body {
    width: 1200px;
    height: 1000px;
    overflow: hidden;
    background: var(--page-bg);
  }
  body {
    position: relative;
    font-family: "Arimo", Helvetica, Arial, sans-serif;
  }
  .business-card {
    position: absolute;
    left: 56px;
    top: 31px;
    width: 1087px;
    height: 637px;
    background: var(--card-bg);
    border: 1px solid var(--card-border);
  }
  .brand-area {
    position: absolute;
    left: 0;
    top: 0;
    width: 100%;
    height: 319px;
    display: flex;
    align-items: center;
    justify-content: center;
  }
  .brand-name {
    color: var(--brand-slate);
    font-weight: 700;
    text-align: center;
    text-transform: uppercase;
    line-height: 1;
  }
  .brand-name .brand-primary {
    display: block;
    font-size: 112px;
    letter-spacing: 4px;
  }
  .brand-name .brand-secondary {
    display: block;
    font-size: 52px;
    letter-spacing: 3px;
    margin-top: 14px;
  }
  .contact-band {
    position: absolute;
    left: 0;
    top: 319px;
    width: 100%;
    height: 226px;
    background: linear-gradient(to bottom, var(--band-top), var(--band-bottom));
    color: var(--text-light);
    text-align: center;
  }
  .agent-name {
    position: absolute;
    left: 0;
    right: 0;
    top: 20px;
    font-size: 41px;
    font-weight: 700;
    letter-spacing: -0.5px;
    text-transform: uppercase;
  }
  .contact-list {
    position: absolute;
    left: 0;
    right: 0;
    top: 86px;
    list-style: none;
    font-size: 28px;
    line-height: 33.5px;
    font-weight: 400;
  }
  .site-footer {
    position: absolute;
    left: 0;
    top: 545px;
    width: 100%;
    height: 69px;
    background: linear-gradient(to bottom, var(--footer-top), var(--footer-bottom));
    color: var(--text-light);
    text-align: center;
    font-size: 28px;
    line-height: 64px;
  }
</style>
</head>
<body>
  <article class="business-card">
    <header class="brand-area">
      <h1 class="brand-name">
        <span class="brand-primary">Tarvo</span>
        <span class="brand-secondary">Commercial</span>
      </h1>
    </header>

    <section class="contact-band">
      <h2 class="agent-name">Colin Farrow</h2>
      <ul class="contact-list">
        <li class="license">lic# 07281549</li>
        <li class="phone">415.555.0172</li>
        <li class="email">colin@tarvo-commercial.example</li>
      </ul>
    </section>

    <footer class="site-footer">tarvo-commercial.example</footer>
  </article>
</body>
</html>
```